Nobre Lente Lusitana - business card

Create a business card for my eyewear (glasses) store. The concept is based in handcrafted glasses (as well as common frames and 3d printed), clean, and elegant. The business card could be black (white letters and symbols) or white (black letters and symbols) but we are open to new suggestions. It must be sober and elegant.
The name Nobre Lente Lusitana means Royal/Real Portuguese Optical Store.
Our concept should be inspired by the pictures attatched bellow.
I would like it to be classic and elegant as business cards for bankers.
Our first selected logo is also available in attachment files.

Target Market(s)

For business meetings with investors, supliers and fairs

Industry/Entity Type

Eyewear

Contact Information for Business Card

Some random business cards in attachment that we like. Don't be closed to it, we like freedom of think.

Font styles to use
Serif
Sans Serif

Colors
404040
e9e9e9
fbfbfb
000000
85abd3
0255a3
f7fbfd
959595

Requirements
Must have
• Must be elegant, simple.
• Must present our brand new logo (slight variations are welcome, the logo is not closed yet). See our temporary logo in attachment.
• Black (or dark grey), white (or light grey) and a third slight color.
• This third slight color could be dark blue or grayish blue.
• Info:
• Tomás Vidigal (name)
• tvidigal@nobrelentelusitana.example
• +351 927364051
• www.nobrelentelusitana.example
Nice to have
• Black and white or with serious colors such as dark blue or greyish blue.
• Could also have water mark with our logo (big size) in the background (inspired in KMT bank credit card design)
Should not have
• Hysteric colora or shapes

```html
<!DOCTYPE html>
<html lang="pt">
<head>
<meta charset="utf-8">
<title>Nobre Lente Lusitana – Cartão de visita</title>
<link href="https://fonts.googleapis.com/css2?family=Roboto+Slab:wght@600&family=Oswald:wght@500&family=Open+Sans:wght@400&display=swap" rel="stylesheet">
<style>
  :root {
    --backdrop: #161616;
    --card: #1e1e1e;
    --card-edge: #2a2a2a;
    --ink-light: #e9e9e9;
    --ink-soft: #c8c8c8;
    --rule: #bdbdbd;
  }
  * { margin: 0; padding: 0; box-sizing: border-box; }
  html, body {
    width: 1200px;
    height: 896px;
    overflow: hidden;
    background: var(--backdrop);
  }
  .stage {
    position: relative;
    width: 1200px;
    height: 896px;
  }
  .card {
    position: absolute;
    width: 486px;
    height: 276px;
    border-radius: 17px;
    background: var(--card);
    border: 1px solid var(--card-edge);
  }
  .card--front { left: 355px; top: 162px; }
  .card--back  { left: 352px; top: 470px; }

  .brand {
    position: absolute;
    left: 0; right: 0;
    top: 62px;
    text-align: center;
    font-family: "Roboto Slab", serif;
    font-weight: 600;
    font-size: 30px;
    line-height: 44px;
    letter-spacing: 0.28em;
    color: var(--ink-light);
    text-transform: uppercase;
  }
  .brand span { display: block; }

  .website {
    position: absolute;
    left: 0; right: 0;
    top: 242px;
    text-align: center;
    font-family: "Open Sans", sans-serif;
    font-size: 11px;
    color: var(--ink-soft);
  }

  .contact {
    position: absolute;
    left: 60px;
    top: 124px;
    display: flex;
    align-items: center;
  }
  .contact__name {
    font-family: "Oswald", sans-serif;
    font-weight: 500;
    font-size: 21px;
    letter-spacing: 0.02em;
    color: var(--ink-light);
    text-transform: uppercase;
  }
  .contact__rule {
    width: 1px;
    height: 26px;
    background: var(--rule);
    margin: 0 9px 0 11px;
  }
  .contact__details {
    font-family: "Open Sans", sans-serif;
    font-size: 11px;
    line-height: 14px;
    color: var(--ink-soft);
  }
</style>
</head>
<body>
  <main class="stage">
    <section class="card card--front" aria-label="Frente do cartão">
      <h1 class="brand">
        <span>Nobre</span>
        <span>Lente</span>
        <span>Lusitana</span>
      </h1>
      <p class="website">www.nobrelentelusitana.example</p>
    </section>

    <section class="card card--back" aria-label="Verso do cartão">
      <div class="contact">
        <p class="contact__name">Tomás Vidigal</p>
        <div class="contact__rule"></div>
        <div class="contact__details">
          <p>+351 927364051</p>
          <p>tvidigal@nobrelentelusitana.example</p>
        </div>
      </div>
    </section>
  </main>
</body>
</html>
```